Brook & Thistle Labels*

Hello :) I am needing labels for my herbal tea/petal product. I am a small producer for the local restaurants (edible flowers/micro herbs & dried product). I am hoping to sell the dried product online. It will be sold in batches as it is ready so quite small/boutique and the label needs to be somewhat generic for the range of produce I make.
Feels: no/minimal plastic, product is in a reusable mason jar, we use organic/regenerative principles from soil health to end product. Treading gently on the land. High quality i.e only fresh hand picked leaf tips for the tea.

```html
<!DOCTYPE html>
<html lang="en">
<head>
<meta charset="utf-8">
<title>Brook &amp; Thistle – Tea Labels</title>
<link href="https://fonts.googleapis.com/css2?family=Special+Elite&family=Oswald:wght@500&family=Delius&family=Courier+Prime&family=Lobster&family=Varela+Round&display=swap" rel="stylesheet">
<style>
  :root {
    --page: #ffffff;
    --linen: #e9e9e8;
    --linen-dark: #dcdcdb;
    --ink: #111111;
    --board: #050505;
    --leaf: #1f8a3c;
    --leaf-light: #5db552;
    --chalk: #ffffff;
    --bloom-light: #f2eef1;
    --bloom-tone: #c9b4c4;
    --rule: #6d6d6d;
    --flag: #1f2e86;
  }
  * { margin: 0; padding: 0; box-sizing: border-box; }
  html, body { width: 1200px; height: 849px; overflow: hidden; background: var(--page); }
  .sheet { position: relative; width: 1200px; height: 849px; }

  .label {
    position: absolute;
    background:
      repeating-linear-gradient(0deg, rgba(0,0,0,.025) 0 1px, transparent 1px 3px),
      repeating-linear-gradient(90deg, rgba(0,0,0,.02) 0 1px, transparent 1px 3px),
      linear-gradient(135deg, var(--linen), var(--linen-dark));
    box-shadow: 0 2px 5px rgba(0,0,0,.22);
  }
  .label--tall { left: 73px; top: 148px; width: 358px; height: 536px; }
  .label--wide { left: 471px; top: 393px; width: 352px; height: 292px; }
  .label--info { left: 861px; top: 392px; width: 295px; height: 293px; }

  .brand { position: absolute; left: 0; right: 0; text-align: center; }
  .brand__dot { display: block; margin: 0 auto; border-radius: 50%;
    background: radial-gradient(circle at 60% 35%, var(--leaf-light), var(--leaf)); }
  .brand__name { display: block; font-family: "Varela Round", sans-serif; color: var(--ink); line-height: 1; }
  .label--tall .brand { top: 15px; }
  .label--tall .brand__dot { width: 86px; height: 86px; }
  .label--tall .brand__name { font-size: 29px; margin-top: 14px; }
  .label--wide .brand { top: 10px; }
  .label--wide .brand__dot { width: 50px; height: 50px; }
  .label--wide .brand__name { font-size: 17px; margin-top: 9px; }

  .board { position: absolute; }
  .board__frame { position: absolute; inset: -6px -4px 4px -8px; border: 2px solid var(--leaf); border-radius: 8px 10px 6px 8px; }
  .board__slate { position: absolute; inset: 0; background: var(--board); border-radius: 4px 8px 3px 6px; }
  .board__title { position: relative; z-index: 2; font-family: "Special Elite", monospace; font-weight: 400; color: var(--chalk); line-height: 1; }
  .label--tall .board { left: 38px; top: 152px; width: 286px; height: 229px; }
  .label--tall .board__title { padding-top: 30px; text-align: center; }
  .label--tall .title-top { display: block; font-size: 54px; }
  .label--tall .title-amp { display: block; font-size: 34px; margin: 8px 0 6px; }
  .label--tall .title-bottom { display: block; font-size: 44px; padding-left: 30px; }
  .label--wide .board { left: 63px; top: 90px; width: 228px; height: 110px; }
  .label--wide .board__title { padding-top: 16px; text-align: left; }
  .label--wide .title-top { display: block; font-size: 30px; padding-left: 36px; }
  .label--wide .title-bottom { display: block; font-size: 30px; margin-top: 16px; padding-left: 80px; }

  .blooms { position: absolute; z-index: 1; border-radius: 50% 46% 52% 48%;
    background: linear-gradient(150deg, var(--bloom-light), var(--bloom-tone)); }
  .label--tall .blooms { left: 14px; top: 312px; width: 98px; height: 90px; }
  .label--wide .blooms { left: 31px; top: 115px; width: 94px; height: 100px; }

  .claim { position: absolute; left: 0; right: 0; text-align: center; font-family: "Oswald", sans-serif; font-weight: 500; color: var(--leaf); text-transform: uppercase; line-height: 1; }
  .label--tall .claim { top: 404px; font-size: 22px; }
  .label--wide .claim { top: 210px; font-size: 17px; }

  .origin { position: absolute; left: 0; right: 0; text-align: center; font-family: "Delius", cursive; color: var(--ink); white-space: nowrap; }
  .label--tall .origin { top: 455px; font-size: 19px; line-height: 29px; }
  .label--wide .origin { top: 233px; font-size: 16px; line-height: 25px; }

  .facts { position: absolute; left: 23px; top: 30px; width: 247px; border-collapse: collapse; font-family: "Courier Prime", monospace; font-size: 12px; color: var(--ink); }
  .facts td, .facts th { border: 1px solid var(--rule); vertical-align: top; text-align: left; padding: 6px 9px; line-height: 15px; }
  .facts th { font-family: "Lobster", cursive; font-weight: 400; font-size: 19px; height: 40px; padding: 8px 9px; }
  .facts .col-key { width: 123px; }
  .row-leaf td { height: 58px; }
  .row-petals td, .row-batch td { height: 37px; padding-top: 9px; }
  .row-place td { height: 55px; padding-top: 13px; }
  .flag { display: inline-block; width: 53px; height: 28px; background: var(--flag); float: right; margin-top: 2px; margin-right: 18px; }
</style>
</head>
<body>
<main class="sheet">

  <section class="label label--tall">
    <div class="brand"><span class="brand__dot"></span><span class="brand__name">fernhollow</span></div>
    <div class="board">
      <span class="board__frame"></span><span class="board__slate"></span>
      <h1 class="board__title"><span class="title-top">BROOK</span><span class="title-amp">&amp;</span><span class="title-bottom">THISTLE</span></h1>
    </div>
    <div class="blooms" role="img" aria-label="Photo of a small cluster of white and purple cornflowers"></div>
    <p class="claim">Chemical Free</p>
    <p class="origin">Grown, harvested and dried<br>on our farm in Tallowood Vale</p>
  </section>

  <section class="label label--wide">
    <div class="brand"><span class="brand__dot"></span><span class="brand__name">fernhollow</span></div>
    <div class="board">
      <span class="board__frame"></span><span class="board__slate"></span>
      <h1 class="board__title"><span class="title-top">BROOK &amp;</span><span class="title-bottom">THISTLE</span></h1>
    </div>
    <div class="blooms" role="img" aria-label="Photo of a small cluster of white and purple cornflowers"></div>
    <p class="claim">Chemical Free</p>
    <p class="origin">Grown, harvested and dried<br>on our farm in Tallowood Vale</p>
  </section>

  <section class="label label--info">
    <table class="facts">
      <tr><th colspan="2">Single Origin Herbal Tee</th></tr>
      <tr class="row-leaf"><td class="col-key">Leaf base</td><td>Lemon<br>Verbena<br>Agastache</td></tr>
      <tr class="row-petals"><td class="col-key">Petals</td><td></td></tr>
      <tr class="row-batch"><td class="col-key">Batch</td><td></td></tr>
      <tr class="row-place"><td colspan="2"><span class="flag" role="img" aria-label="Australian flag"></span>Wattle Bend<br>Victoria Australia</td></tr>
    </table>
  </section>

</main>
</body>
</html>
```